Landing Page Design

Require a landing page design.

A wire concept has been provided along with a relevant logo and image files.

Target Market(s)

Facilities/Property Management companies
Maintenance Managers for manufacturing and related sites
Personal Assistants (those given responsible for the maintenance and cleaning of commercial properties

Industry/Entity Type

Construction

Number of Pages Required

1 page

Requirements
Must have
• 1. Layout as per wire design concept
2. Stick to colour scheme of logo and include plenty of white space
Should not have
• No flash

```html
<!DOCTYPE html>
<html lang="en">
<head>
<meta charset="utf-8">
<title>Veranta – Free Window & Carpet Clean</title>
<link href="https://fonts.googleapis.com/css2?family=Cabin:wght@400;500;600&family=Roboto:wght@300;400;500;700&display=swap" rel="stylesheet">
<style>
  :root {
    --brand-blue: #0b4f9e;
    --deep-blue: #0d3c78;
    --text-blue: #0b3f86;
    --mid-blue: #3a8fd6;
    --panel-grey: #cfd6df;
    --testimonial: #8ea3bf;
    --testimonial-head: #8098b8;
    --page-grey: #e8e9eb;
    --footer-grey: #bdbdbd;
    --green: #6ab42d;
    --green-dark: #4e9a1c;
    --green-text: #3f8a16;
    --grey-text: #7d7f83;
    --body-text: #4a4d52;
    --white: #ffffff;
  }
  * { box-sizing: border-box; margin: 0; padding: 0; }
  html, body { width: 1200px; height: 2769px; overflow: hidden; background: var(--page-grey); }
  body { font-family: "Roboto", Arial, sans-serif; color: var(--body-text); }

  .page {
    position: relative; width: 1200px; height: 1384.5px; overflow: hidden;
    background: linear-gradient(to bottom, var(--brand-blue) 0, #1a5ea8 180px, #6f9ccb 330px, #c6d5e5 420px, var(--page-grey) 480px, var(--page-grey) 100%);
  }
  .abs { position: absolute; }

  .brand { left: 76px; top: 20px; display: flex; align-items: center; gap: 8px; }
  .brand-mark { width: 22px; height: 22px; background: var(--white); }
  .brand-name { font-family: "Roboto", sans-serif; font-weight: 700; font-size: 28px; color: var(--white); letter-spacing: 1px; }

  .hero-frame { left: 74px; top: 91px; width: 698px; height: 414px; background: var(--deep-blue); }
  .hero-photo {
    position: absolute; left: 11px; top: 11px; width: 676px; height: 346px;
    background: linear-gradient(to bottom, #bfe3f7 0%, #d9d9d9 14%, #3a6fb5 30%, #1d4f93 65%, #2f5e2a 88%, #4f7a2a 100%);
  }
  .hero-nav { position: absolute; left: 0; bottom: 0; width: 100%; height: 44px; display: flex; justify-content: center; align-items: center; }
  .hero-nav span { color: #b7cde8; font-size: 15.5px; padding: 0 22px; border-left: 1px solid #3b6aa3; line-height: 26px; }
  .hero-nav span:first-child { border-left: none; }

  .offer {
    left: 592px; top: 156px; width: 535px; height: 234px;
    background: linear-gradient(to bottom, #ffffff, #e6e7e9);
    border: 3px solid var(--brand-blue); outline: 2px solid var(--white); outline-offset: -6px;
    padding: 24px 0 0 48px; font-family: "Cabin", sans-serif;
  }
  .offer-title { color: var(--green-dark); font-size: 60px; line-height: 72px; font-weight: 500; letter-spacing: -1.5px; }
  .offer-title .amp { font-size: 66px; }
  .offer-call { color: var(--grey-text); font-size: 33px; margin-top: 4px; }

  .intro { left: 74px; top: 526px; width: 700px; }
  .lead { color: var(--text-blue); font-size: 21.5px; line-height: 24px; margin-bottom: 24px; }
  .body-copy { font-size: 14px; line-height: 20px; font-weight: 300; color: #3a3d42; margin-bottom: 19px; }
  .pull { font-size: 18px; line-height: 24px; color: var(--grey-text); }

  .reasons { left: 74px; top: 830px; width: 698px; }
  .reasons-head { height: 61px; background: var(--deep-blue); font-family: "Cabin", sans-serif; font-size: 33px; padding: 10px 18px; color: var(--white); font-weight: 600; border-bottom: 3px solid #7894b8; }
  .reasons-head em { font-style: normal; font-weight: 400; color: var(--mid-blue); }
  .reasons-list { background: var(--panel-grey); height: 229px; list-style: none; padding: 18px 22px; }
  .reasons-list li { display: flex; align-items: center; gap: 18px; height: 39.3px; font-size: 14.5px; font-weight: 300; color: #4a4d52; }
  .num { width: 27px; height: 27px; border-radius: 50%; background: var(--deep-blue); border: 2px solid var(--white); color: var(--white); font-size: 13px; display: flex; align-items: center; justify-content: center; }

  .cta { top: 1143px; width: 233px; height: 88px; background: linear-gradient(to bottom, var(--green), var(--green-dark)); border: 2px solid #8fcc55; color: #2c5a10; font-family: "Cabin", sans-serif; font-size: 24px; line-height: 30px; text-align: center; display: flex; align-items: center; justify-content: center; }
  .cta-quote { left: 145px; }
  .cta-site { left: 468px; }

  .closing { left: 74px; top: 1250px; width: 700px; color: var(--text-blue); font-size: 18px; line-height: 24.5px; }

  .enquiry { left: 792px; top: 461px; width: 335px; height: 443px; background: var(--white); border: 1px solid var(--green); }
  .enquiry-head { background: var(--green); height: 92px; padding: 11px 14px; color: #eef7e4; font-size: 16px; line-height: 24px; font-weight: 300; }
  .enquiry-head strong { color: var(--white); font-weight: 500; font-size: 18px; }
  .enquiry-form { padding: 14px 14px; }
  .field-label { display: block; font-size: 14px; font-weight: 500; color: #222; margin: 0 0 6px; }
  .field { display: block; width: 301px; height: 35px; border: 1px solid #cfd2d6; margin-bottom: 17px; }
  .submit { width: 98px; height: 35px; background: linear-gradient(to bottom, #bdbdbd, #8e8e8e); border: 1px solid #888; color: #333; font-weight: 700; font-size: 14px; display: flex; align-items: center; justify-content: center; margin-top: 2px; }

  .testimonials { left: 793px; top: 925px; width: 335px; height: 246px; background: var(--testimonial); }
  .testimonials-head { height: 56px; background: var(--testimonial-head); border-bottom: 1px solid #a7b8cf; font-family: "Cabin", sans-serif; font-size: 33px; color: var(--white); padding: 8px 14px; }
  .quote-mark { font-family: Georgia, serif; font-size: 50px; color: var(--deep-blue); line-height: 1; font-weight: 700; }
  .quote-open { position: absolute; left: 21px; top: 70px; }
  .quote-close { position: absolute; right: 22px; top: 198px; }
  .testimonial-text { position: absolute; left: 22px; top: 113px; width: 300px; font-size: 12.5px; line-height: 19.7px; color: #1f2b3c; font-weight: 300; }

  .footer { left: 0; top: 1354px; width: 1200px; height: 31px; background: var(--footer-grey); color: #333; font-size: 11.5px; text-align: center; line-height: 31px; }
</style>
</head>
<body>

<section class="page">
  <div class="abs brand"><span class="brand-mark"></span><span class="brand-name">VERANTA</span></div>
  <div class="abs hero-frame">
    <div class="hero-photo" role="img" aria-label="Window cleaners on ladders at a glass office building"></div>
    <nav class="hero-nav"><span>NO CONTRACTS</span><span>ROUTINE OFFICE CLEANING</span><span>PAINLESS EXPERIENCE</span></nav>
  </div>
  <div class="abs offer">
    <div class="offer-title">FREE WINDOW<br><span class="amp">&amp;</span> CARPET CLEAN</div>
    <div class="offer-call">Call NOW on 1300 55 01 99</div>
  </div>
  <div class="abs intro">
    <p class="lead">Engage our routine office cleaning for at least 6 months and receive a FREE Carpet and Window clean! No strings attached, no contracts.</p>
    <p class="lead">To take advantage of this great offer call us on 1300 55 01 99 or complete and submit the form on this page.</p>
    <p class="body-copy">At Veranta we provide all your property service needs - painlessly. We understand that cleaning and other property services should be background activities.  A set and forget proposition.</p>
    <p class="body-copy">We also know that you should not have to police or project manage our Service Teams.</p>
    <p class="pull">After engaging Veranta, property services will become your lowest priority, as it is our highest priority.</p>
  </div>
  <div class="abs reasons">
    <h2 class="reasons-head">TOP 5 <em>REASONS TO CHOOSE VERANTA</em></h2>
    <ol class="reasons-list">
      <li><span class="num">1</span>We self audit and performance manage our Service Teams while they're on the job</li>
      <li><span class="num">2</span>We minimise contact time required between the client and our Service Teams</li>
      <li><span class="num">3</span>Our Service Teams are proactive in identifying irregular requirements</li>
      <li><span class="num">4</span>We have a comprehensive Health Safety Management system</li>
      <li><span class="num">5</span>We can provide our Property Services on a National basis</li>
    </ol>
  </div>
  <div class="abs cta cta-quote">BOOK A<br>FREE QUOTE</div>
  <div class="abs cta cta-site">VISIT OUR<br>WEB SITE</div>
  <p class="abs closing">If you would like to join our growing list of satisfied clients, call NOW to discuss how Veranta can best meet all your Commercial Cleaning and Property Service needs.</p>
  <div class="abs enquiry">
    <div class="enquiry-head">Take advantage of this great offer.<br>Contact Us NOW on <strong>1300 55 01 99</strong><br>or register your interest below.</div>
    <div class="enquiry-form">
      <span class="field-label">Name</span><span class="field"></span>
      <span class="field-label">Business Name</span><span class="field"></span>
      <span class="field-label">E - mail</span><span class="field"></span>
      <span class="field-label">Phone</span><span class="field"></span>
      <span class="submit">SUBMIT</span>
    </div>
  </div>
  <div class="abs testimonials">
    <div class="testimonials-head">TESTIMONIALS</div>
    <span class="quote-mark quote-open">&ldquo;</span>
    <p class="testimonial-text">Lorem ipsum dolor sit amet, consectetur adipiscing elit. Fusce mattis placerat tellus, faucibus ornare lacus iaculis sit amet. Praesent et dui sed mauris semper posuere. Sed malesuada lacinia nulla.</p>
    <span class="quote-mark quote-close">&rdquo;</span>
  </div>
  <div class="abs footer">© 2009 Veranta. All rights reserved</div>
</section>

<section class="page">
  <div class="abs brand"><span class="brand-mark"></span><span class="brand-name">VERANTA</span></div>
  <div class="abs hero-frame">
    <div class="hero-photo" role="img" aria-label="Window cleaners on ladders at a glass office building"></div>
    <nav class="hero-nav"><span>NO CONTRACTS</span><span>ROUTINE OFFICE CLEANING</span><span>PAINLESS EXPERIENCE</span></nav>
  </div>
  <div class="abs offer">
    <div class="offer-title">FREE WINDOW<br><span class="amp">&amp;</span> CARPET CLEAN</div>
    <div class="offer-call">Call NOW on 1300 55 01 99</div>
  </div>
  <div class="abs intro">
    <p class="lead">Engage our routine office cleaning for at least 6 months and receive a FREE Carpet and Window clean! No strings attached, no contracts.</p>
    <p class="lead">To take advantage of this great offer call us on 1300 55 01 99 or complete and submit the form on this page.</p>
    <p class="body-copy">At Veranta we provide all your property service needs - painlessly. We understand that cleaning and other property services should be background activities.  A set and forget proposition.</p>
    <p class="body-copy">We also know that you should not have to police or project manage our Service Teams.</p>
    <p class="pull">After engaging Veranta, property services will become your lowest priority, as it is our highest priority.</p>
  </div>
  <div class="abs reasons">
    <h2 class="reasons-head">TOP 5 <em>REASONS TO CHOOSE VERANTA</em></h2>
    <ol class="reasons-list">
      <li><span class="num">1</span>We self audit and performance manage our Service Teams while they're on the job</li>
      <li><span class="num">2</span>We minimise contact time required between the client and our Service Teams</li>
      <li><span class="num">3</span>Our Service Teams are proactive in identifying irregular requirements</li>
      <li><span class="num">4</span>We have a comprehensive Health Safety Management system</li>
      <li><span class="num">5</span>We can provide our Property Services on a National basis</li>
    </ol>
  </div>
  <div class="abs cta cta-quote">BOOK A<br>FREE QUOTE</div>
  <div class="abs cta cta-site">VISIT OUR<br>WEB SITE</div>
  <p class="abs closing">If you would like to join our growing list of satisfied clients, call NOW to discuss how Veranta can best meet all your Commercial Cleaning and Property Service needs.</p>
  <div class="abs enquiry">
    <div class="enquiry-head">Take advantage of this great offer.<br>Contact Us NOW on <strong>1300 55 01 99</strong><br>or register your interest below.</div>
    <div class="enquiry-form">
      <span class="field-label">Name</span><span class="field"></span>
      <span class="field-label">Business Name</span><span class="field"></span>
      <span class="field-label">E - mail</span><span class="field"></span>
      <span class="field-label">Phone</span><span class="field"></span>
      <span class="submit">SUBMIT</span>
    </div>
  </div>
  <div class="abs testimonials">
    <div class="testimonials-head">TESTIMONIALS</div>
    <span class="quote-mark quote-open">&ldquo;</span>
    <p class="testimonial-text">Lorem ipsum dolor sit amet, consectetur adipiscing elit. Fusce mattis placerat tellus, faucibus ornare lacus iaculis sit amet. Praesent et dui sed mauris semper posuere. Sed malesuada lacinia nulla.</p>
    <span class="quote-mark quote-close">&rdquo;</span>
  </div>
  <div class="abs footer">© 2009 Veranta. All rights reserved</div>
</section>

</body>
</html>
```